The maple crew

I want it as prefession and attractive as possible we are a lawnmowing business

Phone number 605-318-2264
Name- Carlos Whitfield
Email- themaplecrewsd@fernpost.com

```html
<!DOCTYPE html>
<html lang="en">
<head>
<meta charset="utf-8">
<title>The Maple Crew – Business Card</title>
<link rel="stylesheet" href="https://fonts.googleapis.com/css2?family=Teko:wght@500;600&family=Roboto:wght@400;700&display=swap">
<style>
  :root {
    --page-bg: #e9e9e9;
    --card-green: #115e39;
    --accent-green: #5dbb46;
    --white: #ffffff;
  }
  * { margin: 0; padding: 0; box-sizing: border-box; }
  html, body {
    width: 1200px;
    height: 1200px;
    overflow: hidden;
    background: var(--page-bg);
  }
  .card {
    position: absolute;
    left: 225px;
    width: 749px;
    height: 449px;
    background: var(--card-green);
  }
  .card--front { top: 120px; }
  .card--back { top: 631px; }

  .brand-title {
    position: absolute;
    left: 51px;
    top: 44px;
    font-family: "Teko", "Oswald", sans-serif;
    font-weight: 500;
    font-size: 64px;
    line-height: 1;
    letter-spacing: 1px;
    text-transform: uppercase;
    color: var(--accent-green);
  }
  .person-name {
    position: absolute;
    left: 51px;
    top: 224px;
    font-family: "Roboto", Arial, sans-serif;
    font-weight: 700;
    font-size: 35px;
    line-height: 1;
    letter-spacing: -0.5px;
    text-transform: uppercase;
    color: var(--white);
  }
  .name-rule {
    position: absolute;
    left: 51px;
    top: 274px;
    width: 637px;
    height: 6px;
    background: var(--white);
  }
  .mowing-illustration {
    position: absolute;
    left: 448px;
    top: 196px;
    width: 252px;
    height: 80px;
    border-radius: 4px;
    background: linear-gradient(90deg, rgba(255,255,255,0.85), rgba(255,255,255,0.55));
  }
  .contact-list {
    position: absolute;
    left: 50px;
    top: 328px;
    list-style: none;
    font-family: "Roboto", Arial, sans-serif;
    font-size: 25px;
    color: var(--accent-green);
  }
  .contact-item {
    display: flex;
    align-items: center;
    height: 38px;
  }
  .contact-icon {
    width: 20px;
    height: 20px;
    margin-right: 15px;
    flex: none;
  }
  .back-name {
    position: absolute;
    inset: 0;
    display: flex;
    align-items: center;
    justify-content: center;
    font-family: "Teko", "Oswald", sans-serif;
    font-weight: 600;
    font-size: 110px;
    line-height: 1;
    text-transform: uppercase;
    color: var(--accent-green);
    padding-top: 14px;
  }
</style>
</head>
<body>
  <section class="card card--front">
    <h1 class="brand-title">The Maple Crew</h1>
    <p class="person-name">Carlos Whitfield</p>
    <div class="name-rule"></div>
    <div class="mowing-illustration" role="img" aria-label="White silhouette of a worker pushing a lawn mower through tall grass"></div>
    <ul class="contact-list">
      <li class="contact-item">
        <svg class="contact-icon" viewBox="0 0 24 24" aria-hidden="true">
          <path fill="#ffffff" d="M6.6 10.8a15.1 15.1 0 0 0 6.6 6.6l2.2-2.2a1 1 0 0 1 1-.25 11.4 11.4 0 0 0 3.6.57 1 1 0 0 1 1 1V20a1 1 0 0 1-1 1A17 17 0 0 1 3 4a1 1 0 0 1 1-1h3.5a1 1 0 0 1 1 1c0 1.25.2 2.45.57 3.6a1 1 0 0 1-.25 1z"/>
          <path fill="none" stroke="#ffffff" stroke-width="1.6" d="M14 3.5a7 7 0 0 1 6.5 6.5M14 7a3.5 3.5 0 0 1 3 3"/>
        </svg>
        <span>605-318-2264</span>
      </li>
      <li class="contact-item">
        <svg class="contact-icon" viewBox="0 0 24 24" aria-hidden="true">
          <rect x="2" y="5" width="20" height="14" fill="none" stroke="#ffffff" stroke-width="2"/>
          <path d="M2 5l10 8 10-8M2 19l7.5-7M22 19l-7.5-7" fill="none" stroke="#ffffff" stroke-width="1.6"/>
        </svg>
        <span>themaplecrewsd@fernpost.com</span>
      </li>
    </ul>
  </section>

  <section class="card card--back">
    <p class="back-name">The Maple Crew</p>
  </section>
</body>
</html>
```